Bourbon label design for bourbon brand. Looking to freshen our current label.

I need a Bourbon label design for our rebranded Bourbon bottle. Label should include picture of our horse and our logo on the bottle. Front Label is 3.5 inches wide and 6 inches tall, back label is 4 inches tall and 3 inches wide. Back label can be a simple plain logo like the one in the brief. I have included a design of our current bottle and label. We want to stay close to the current color schemes but want a fresh rebrand of the design. The label needs to be the correct size on a tall bottle like pictured.

Target Market(s)

Our Bourbon members, 30-50 year old males

Requirements
Must have
• Picture of our horse, our B logo , straight Bourbon whiskey on the front. Room to edit text on the back label.

```html
<!DOCTYPE html>
<html lang="en">
<head>
<meta charset="utf-8">
<title>Nightfall Straight Bourbon Whiskey — Front Label</title>
<link rel="stylesheet" href="https://fonts.googleapis.com/css2?family=Crimson+Pro:wght@400;500&display=swap">
<style>
  :root {
    --label-black: #000000;
    --ink-white: #ffffff;
    --photo-light: #bdbdbd;
    --photo-mid: #7a7a7a;
    --photo-dark: #2a2a2a;
  }
  html, body {
    margin: 0;
    padding: 0;
    width: 700px;
    height: 1200px;
    overflow: hidden;
    background: var(--label-black);
  }
  .label {
    position: relative;
    width: 700px;
    height: 1200px;
    background: var(--label-black);
    color: var(--ink-white);
    font-family: "Crimson Pro", Georgia, serif;
  }
  .label > * { position: absolute; margin: 0; }

  .hero-horse {
    left: 266px;
    top: 63px;
    width: 180px;
    height: 368px;
    border-radius: 45% 45% 30% 30% / 20% 20% 12% 12%;
    background: radial-gradient(ellipse at 50% 35%, var(--photo-light) 0%, var(--photo-mid) 45%, var(--photo-dark) 85%, var(--label-black) 100%);
  }

  .est-mark {
    top: 250px;
    font-size: 24px;
    line-height: 1;
    width: 120px;
    text-align: center;
  }
  .est-mark--word { left: 144px; }
  .est-mark--year { left: 434px; }

  .brand-name {
    left: 0;
    top: 478px;
    width: 700px;
    text-align: center;
    font-size: 112px;
    font-weight: 500;
    line-height: 1;
    letter-spacing: 2px;
    text-transform: uppercase;
  }

  .spirit-type {
    left: 0;
    top: 648px;
    width: 694px;
    text-align: center;
    font-size: 35px;
    line-height: 1;
  }

  .feature {
    top: 803px;
    font-size: 20px;
    line-height: 1;
    width: 200px;
    text-align: center;
  }
  .feature--barrel { left: 62px; }
  .feature--strength { left: 446px; }

  .brand-mark {
    left: 250px;
    top: 810px;
    width: 200px;
    text-align: center;
    font-size: 26px;
    font-weight: 500;
    line-height: 1;
  }
  .brand-mark__dot {
    display: block;
    width: 44px;
    height: 44px;
    margin: 0 auto 12px;
    border: 2px solid var(--ink-white);
    border-radius: 50%;
  }

  .spec {
    text-align: center;
  }
  .spec__title {
    display: block;
    font-size: 17px;
    letter-spacing: 1.5px;
    line-height: 1;
    margin-bottom: 4px;
  }
  .spec__field {
    display: block;
    background: var(--ink-white);
    border-radius: 6px;
  }
  .spec--barrel { left: 108px; top: 1041px; }
  .spec--barrel .spec__field { width: 109px; height: 36px; }
  .spec--aged { left: 301px; top: 1024px; }
  .spec--aged .spec__field { width: 96px; height: 62px; }
  .spec--abv { left: 481px; top: 1041px; }
  .spec--abv .spec__field { width: 109px; height: 36px; }
</style>
</head>
<body>
  <main class="label">
    <div class="hero-horse" role="img" aria-label="Black and white photograph of the brand's racehorse galloping toward the viewer with a jockey"></div>

    <p class="est-mark est-mark--word">EST</p>
    <p class="est-mark est-mark--year">2016</p>

    <h1 class="brand-name">Nightfall</h1>
    <p class="spirit-type">Straight Bourbon Whiskey</p>

    <p class="feature feature--barrel">Single Barrel</p>
    <div class="brand-mark">
      <span class="brand-mark__dot"></span>
      Nightfall
    </div>
    <p class="feature feature--strength">Cask Strength</p>

    <div class="spec spec--barrel">
      <span class="spec__title">BARREL NO.</span>
      <span class="spec__field"></span>
    </div>
    <div class="spec spec--aged">
      <span class="spec__title">AGED</span>
      <span class="spec__field"></span>
    </div>
    <div class="spec spec--abv">
      <span class="spec__title">ALC/VOL</span>
      <span class="spec__field"></span>
    </div>
  </main>
</body>
</html>
```